Accounting business needs a fridge magnet design

I need a business card size design to be used as a fridge magnet.
It will need to be vertical not horizontal and it will have my logo and the services I provide listed below it.
It needs to be pleasing to the eye and catch peoples attention.
I have uploaded my current business card as a reference.
It can look totally different though, i am open to new ideas.

It will need to say:

Specialising in:
*Small Business Taxation
*Company & Trust Returns
*Financial Statements
*Partnership Taxation
*BAS preparation/lodgement
*Capital Gains Tax
*Business Start Ups
*Business Structuring
*Tax Planning

```html
<!DOCTYPE html>
<html lang="en">
<head>
<meta charset="utf-8">
<title>Clearline Tax – Fridge Magnet</title>
<link href="https://fonts.googleapis.com/css2?family=Montserrat:wght@400;500;700&display=swap" rel="stylesheet">
<style>
  :root {
    --backdrop: #5b5b5b;
    --card: #ffffff;
    --ink: #1f1e1c;
    --brand-black: #1f1e1c;
    --brand-blue: #22b0e4;
    --heading-blue: #22a9e0;
    --white: #ffffff;
    --badge-green: #b7d433;
    --badge-navy: #1f57a3;
    --badge-yellow: #f2d21a;
  }
  * { box-sizing: border-box; margin: 0; padding: 0; }
  html, body {
    width: 1200px; height: 1200px; overflow: hidden;
    background: var(--backdrop);
    font-family: "Montserrat", sans-serif;
  }
  .magnet {
    position: absolute; left: 307px; top: 86px;
    width: 586px; height: 1027px;
    background: var(--card);
    overflow: hidden;
  }
  .magnet__bands { position: absolute; inset: 0; }
  .brand {
    position: absolute; left: 0; top: 0; width: 100%;
    text-align: center; color: var(--white);
  }
  .brand__mark {
    position: absolute; left: 237px; top: 38px;
    width: 112px; height: 112px;
    border: 3px solid var(--white); border-radius: 50%;
  }
  .brand__name {
    position: absolute; left: 0; top: 166px; width: 100%;
    font-weight: 500; font-size: 34px; letter-spacing: 13px;
    padding-left: 13px; line-height: 42px;
  }
  .services {
    position: absolute; left: 0; top: 258px; width: 100%;
    text-align: center;
  }
  .services__heading {
    color: var(--heading-blue);
    font-weight: 700; font-size: 30px; line-height: 42px; letter-spacing: 0.5px;
  }
  .services__list {
    list-style: none; margin-top: 4px;
    color: var(--ink); font-weight: 500; font-size: 22.5px; line-height: 27.6px;
  }
  .badges {
    position: absolute; left: 0; top: 573px; width: 100%; height: 58px;
  }
  .badge { position: absolute; top: 0; }
  .badge--register {
    left: 157px; width: 57px; height: 57px; border-radius: 50%;
    background: var(--white); border: 2px solid #9a9a9a;
  }
  .badge--register::after {
    content: ""; position: absolute; inset: 10px; border-radius: 50%;
    background: var(--badge-green);
  }
  .badge--body {
    left: 229px; width: 129px; height: 57px;
    background: linear-gradient(90deg, var(--badge-navy) 0 62%, var(--badge-yellow) 62% 100%);
  }
  .badge--software {
    left: 373px; width: 57px; height: 57px; border-radius: 50%;
    background: var(--brand-blue);
  }
  .contact {
    position: absolute; left: 0; top: 688px; width: 100%;
    text-align: center; color: var(--ink);
  }
  .contact__name {
    color: var(--white); font-weight: 700; font-size: 50px; line-height: 64px;
  }
  .contact__role { font-size: 23px; line-height: 31.5px; }
  .contact__divider {
    position: relative; height: 28px; margin-top: 7px;
  }
  .contact__divider .rule {
    position: absolute; top: 13px; height: 2px; width: 149px; background: var(--white);
  }
  .contact__divider .rule--left { left: 74px; }
  .contact__divider .rule--right { left: 366px; }
  .contact__divider svg { position: absolute; top: 0; left: 238px; }
  .contact__details { margin-top: 8px; font-size: 28px; line-height: 37px; }
</style>
</head>
<body>
  <main class="magnet">
    <svg class="magnet__bands" width="586" height="1027" viewBox="0 0 586 1027" aria-hidden="true">
      <path d="M0 0 H586 V162 Q293 324 0 162 Z" fill="var(--brand-black)"/>
      <path d="M0 709 Q293 583 586 709 V1027 H0 Z" fill="var(--brand-blue)"/>
    </svg>

    <header class="brand">
      <div class="brand__mark"></div>
      <div class="brand__name">CLEARLINE TAX</div>
    </header>

    <section class="services">
      <h2 class="services__heading">SPECIALISING IN</h2>
      <ul class="services__list">
        <li>Small Business Taxation</li>
        <li>Company and Trust Returns</li>
        <li>Financial Statements</li>
        <li>Partnership Taxation</li>
        <li>BAS Preparation / Lodgement</li>
        <li>Capital Gains Tax</li>
        <li>Business Start Ups</li>
        <li>Business Structuring</li>
        <li>Tax Planning</li>
      </ul>
    </section>

    <div class="badges" aria-label="Registrations and memberships">
      <span class="badge badge--register"></span>
      <span class="badge badge--body"></span>
      <span class="badge badge--software"></span>
    </div>

    <section class="contact">
      <h1 class="contact__name">OWEN HARTLEY</h1>
      <p class="contact__role">CPA, MTAX, BCOM (Acc &amp; Fin)</p>
      <p class="contact__role">Taxation and Business Accountant</p>
      <p class="contact__role">Tax Agent</p>
      <div class="contact__divider">
        <span class="rule rule--left"></span>
        <svg width="110" height="28" viewBox="0 0 110 28" aria-hidden="true">
          <path d="M6 4 q3 -1 4 2 l1 4 q0 2 -2 3 q1 4 4 7 q1 -2 3 -2 l4 2 q2 2 1 4 l-2 2 q-8 0 -13 -9 q-3 -6 0 -13 Z" fill="var(--white)"/>
          <rect x="41" y="7" width="20" height="14" fill="var(--white)"/>
          <path d="M41 7 L51 15 L61 7" fill="none" stroke="var(--brand-blue)" stroke-width="2"/>
          <circle cx="95" cy="14" r="9" fill="none" stroke="var(--white)" stroke-width="2.2"/>
          <ellipse cx="95" cy="14" rx="4" ry="9" fill="none" stroke="var(--white)" stroke-width="1.8"/>
          <path d="M86 14 H104 M88 9 H102 M88 19 H102" stroke="var(--white)" stroke-width="1.6"/>
        </svg>
        <span class="rule rule--right"></span>
      </div>
      <div class="contact__details">
        <p>0412 555 308</p>
        <p>owen@clearlinetax.com.au</p>
        <p>www.clearlinetax.com.au</p>
      </div>
    </section>
  </main>
</body>
</html>
```